Looking for a modern elegant home improvment website

Looking for a new Design on current website . Please us www.brambleforkbuilders.com PIctures of recent work and stock photos that were attached , Free estimates , Explaining what we do , Similiar to www. brambleforkbuilders.com which is our current webpage . Colors can be different . I have attached our buisness card as well as our postcard we send out to homes . I would like a modern web page that our costumers can feel is professional so they can have a feeling of trust when they hire us . Our address should be on there . Licenesed & Insured should be somewhere on the page . Our Company Logo should be there as well . It would be nice to have a very modern website with great pictures of home interiors and exteriors . a page describing what we do is very important . facebook link to our page is a must as well as a instagram .
Updates

Reason: Looking for a elegant modern 5 page website with proper spelling and professional looking . I extended the deadline and upgraded .

Reason: Looking for more design options .

Target Market(s)

Home owners , Commerical buisness,

Industry/Entity Type

Home Improvement

Number of Pages Required

5+ page

Font styles to use
Serif

Requirements
Must have
• PIctures of recent work and stock photos that were attached , Free estimates , Explaining what we do , Similiar to www. brambleforkbuilders.com which is our current webpage . Colors can be different . I have attached our buisness card as well as our postcard we send out to homes . I would like a modern web page that our costumers can feel is professional so they can have a feeling of trust when they hire us . Our address should be on there . Licenesed & Insured should be somewhere on the page . Our Company Logo should be there as well .
Nice to have
• It would be nice to have a very modern website with great pictures of home interiors and exteriors . a page describing what we do is very important . facebook link to our page is a must as well as a instagram .

```html
<!DOCTYPE html>
<html lang="en">
<head>
<meta charset="utf-8">
<title>Bramble Fork Builders LLC</title>
<link rel="stylesheet" href="https://fonts.googleapis.com/css2?family=Nunito+Sans:wght@300;400;600;700&family=Open+Sans:wght@400;600&display=swap">
<style>
:root{
  --green:#0b5e36;
  --green-mid:#127a45;
  --green-light:#1f8a55;
  --navy:#1e2f5c;
  --ink:#2c2c2c;
  --muted:#8a8a8a;
  --footer:#efefef;
  --white:#ffffff;
}
*{box-sizing:border-box;margin:0;padding:0}
html,body{width:1200px;height:2985px;overflow:hidden}
body{position:relative;background:var(--white);font-family:"Open Sans",sans-serif;color:var(--ink)}
.abs{position:absolute}
h1,h2,h3{font-weight:400}
/* header */
.brand{left:100px;top:24px;display:flex;flex-direction:column;align-items:center;gap:8px;width:350px}
.brand-mark{width:30px;height:30px;border-radius:50%;background:var(--green)}
.brand-name{font-family:"Nunito Sans",sans-serif;font-weight:600;font-size:21px;color:var(--green);letter-spacing:.5px}
.header-contact{left:815px;top:36px;font-family:"Nunito Sans",sans-serif}
.header-contact p{display:flex;align-items:center;gap:8px;color:#333}
.header-contact .phone{font-size:21px}
.header-contact .mail{font-size:16px;margin-top:8px}
.main-nav{left:0;top:118px;width:1200px;height:54px;background:var(--green);display:flex;padding-left:110px}
.main-nav a{font-family:"Nunito Sans",sans-serif;font-weight:600;font-size:16px;color:var(--white);text-decoration:none;line-height:54px;padding:0 32px;border-right:1px solid rgba(255,255,255,.12)}
.main-nav a.active{background:var(--green-light)}
/* photo fills */
.photo-fill{background-blend-mode:normal}
.hero-photo{left:0;top:172px;width:1200px;height:486px;
  background:
    radial-gradient(ellipse 40% 30% at 25% 50%,rgba(214,200,178,.85),rgba(214,200,178,0) 70%),
    radial-gradient(ellipse 35% 25% at 75% 45%,rgba(196,176,150,.7),rgba(196,176,150,0) 70%),
    linear-gradient(180deg,#5a3618 0%,#8a5a2e 30%,#a8774a 55%,#7a4a22 78%,#c08a4e 100%)}
.hero-shade{left:0;top:172px;width:1200px;height:486px;background:linear-gradient(90deg,rgba(40,25,10,.35) 0%,rgba(40,25,10,0) 60%)}
.hero-title{left:118px;top:335px;font-family:"Nunito Sans",sans-serif;font-weight:700;color:var(--white);text-transform:uppercase}
.hero-title .l1{font-size:42px;display:block;line-height:50px}
.hero-title .l2{font-size:33px;display:block;line-height:44px}
.hero-dots{left:555px;top:610px;display:flex;gap:10px}
.hero-dots span{width:15px;height:15px;border-radius:50%;background:var(--white)}
.hero-dots span.on{background:transparent;border:2px solid var(--white)}
/* about */
.section-title{font-family:"Nunito Sans",sans-serif;font-weight:400;text-align:center;width:1200px;left:0}
.about-title{top:702px;font-size:34px;color:#333}
.about-text{left:200px;top:758px;width:800px;text-align:center;font-size:13.5px;line-height:25px;color:var(--muted)}
/* services */
.services-bg{left:0;top:950px;width:1200px;height:455px}
.services-title{top:1018px;font-size:32px;color:var(--white)}
.services-underline{left:500px;top:1066px;width:210px;height:1px;background:rgba(255,255,255,.6)}
.services-underline::after{content:"";position:absolute;left:85px;top:-1px;width:40px;height:3px;background:var(--white)}
.service-card{top:1100px;width:270px;height:215px;clip-path:polygon(9% 0,100% 0,91% 100%,0 100%);overflow:hidden}
.service-card .photo{width:100%;height:100%}
.service-card .caption{position:absolute;left:0;bottom:0;width:100%;height:48px;background:rgba(25,25,25,.78);color:var(--white);font-family:"Nunito Sans",sans-serif;font-size:20px;text-align:center;line-height:48px}
/* why */
.why-photo{left:0;top:1405px;width:600px;height:435px;
  background:
    radial-gradient(ellipse 30% 40% at 45% 40%,rgba(240,238,232,.9),rgba(240,238,232,0) 70%),
    linear-gradient(180deg,#e8e6e1 0%,#d4d0c8 35%,#bdb7ab 52%,#7a5434 62%,#5a3a22 85%,#4a2e1a 100%)}
.why-title{left:650px;top:1470px;font-family:"Nunito Sans",sans-serif;font-weight:400;font-size:29px;color:#333}
.why-text{left:650px;top:1525px;width:430px;font-size:13px;line-height:25px;color:var(--muted)}
.why-text p+p{margin-top:12px}
.btn{left:652px;top:1710px;width:126px;height:38px;background:var(--navy);color:var(--white);border-radius:3px;font-family:"Nunito Sans",sans-serif;font-weight:700;font-size:12px;text-align:center;line-height:38px;letter-spacing:.5px}
/* licensed */
.licensed{left:0;top:1840px;width:1200px;height:400px;background:linear-gradient(160deg,#6f86b8 0%,#4b619a 40%,#263a70 100%)}
.licensed-title{top:1885px;font-size:28px;color:var(--white)}
.licensed-title::before,.licensed-title::after{content:"";display:inline-block;width:55px;height:1px;background:rgba(255,255,255,.6);vertical-align:middle;margin:0 8px}
.trade-list{list-style:none;width:205px}
.trade-list li{font-family:"Nunito Sans",sans-serif;font-size:17px;color:var(--white);height:48px;line-height:48px;border-bottom:1px solid rgba(255,255,255,.25);padding-left:18px;position:relative}
.trade-list li::before{content:"";position:absolute;left:4px;top:20px;border-left:5px solid var(--white);border-top:4px solid transparent;border-bottom:4px solid transparent}
.trade-list li:last-child{border-bottom:none}
/* gallery */
.gallery{left:0;top:2240px;width:1200px;height:390px;background:radial-gradient(ellipse at 50% 10%,#ffffff 40%,#f1f1f1 100%)}
.gallery-title{top:2288px;font-size:32px;color:#333}
.gallery-item{top:2362px;width:232px;height:232px;border-radius:50%;border:3px solid var(--green-mid);padding:6px;background:var(--white)}
.gallery-item .photo{width:100%;height:100%;border-radius:50%}
/* footer */
.site-footer{left:0;top:2630px;width:1200px;height:355px;background:var(--footer)}
.footer-head{font-family:"Nunito Sans",sans-serif;font-weight:400;font-size:23px;color:#333}
.footer-links{list-style:none;font-size:14px;line-height:27px;color:#555}
.footer-contact{font-size:14px;line-height:27px;color:#555}
.footer-contact .row{display:flex;align-items:center;gap:10px}
.socials{left:808px;top:2727px;display:flex;gap:10px}
.socials a{width:38px;height:38px;border-radius:50%;background:var(--green);box-shadow:inset 0 0 0 3px rgba(255,255,255,.18)}
.footer-brand{left:765px;top:2790px;display:flex;flex-direction:column;align-items:center;gap:6px;width:310px}
.footer-brand .brand-mark{width:24px;height:24px}
.footer-brand .brand-name{font-size:18px}
.footer-rule{left:116px;top:2924px;width:968px;height:1px;background:#d8d8d8}
.copyright{left:0;top:2945px;width:1200px;text-align:center;font-size:12px;color:#777}
</style>
</head>
<body>

<header>
  <div class="abs brand">
    <span class="brand-mark"></span>
    <span class="brand-name">Bramble Fork Builders LLC</span>
  </div>
  <div class="abs header-contact">
    <p class="phone"><svg width="18" height="18" viewBox="0 0 24 24"><path fill="#0b5e36" d="M6.6 10.8a15 15 0 006.6 6.6l2.2-2.2a1 1 0 011-.25 11.4 11.4 0 003.6.6 1 1 0 011 1V20a1 1 0 01-1 1A17 17 0 013 4a1 1 0 011-1h3.5a1 1 0 011 1c0 1.25.2 2.45.57 3.57a1 1 0 01-.25 1z"/></svg>(201) 555 0148</p>
    <p class="mail"><svg width="18" height="14" viewBox="0 0 24 18"><rect width="24" height="18" rx="2" fill="#0b5e36"/><path d="M1 2l11 8 11-8" stroke="#fff" stroke-width="2" fill="none"/></svg>hello@brambleforkbuilders.com</p>
  </div>
  <nav class="abs main-nav">
    <a class="active">HOME</a><a>ABOUT US</a><a>SERVICES</a><a>GALLERY</a><a>BLOGS</a><a>CONTACT US</a>
  </nav>
</header>

<section>
  <div class="abs hero-photo" role="img" aria-label="Renovated kitchen with wooden cabinets and granite countertops"></div>
  <div class="abs hero-shade"></div>
  <h1 class="abs hero-title"><span class="l1">Kitchen &amp; Bathroom</span><span class="l2">Renovation &amp; Construction</span></h1>
  <div class="abs hero-dots"><span class="on"></span><span></span><span></span><span></span></div>
</section>

<section>
  <h2 class="abs section-title about-title">About Our Company</h2>
  <p class="abs about-text">Your home is the most important asset you have, so when you're ready to build or remodel, get yourself the best General Contractor in the business! We have been building for over 20 years, specializing in residential construction. We are tile &amp; marble specialist . We build bathrooms , Kitchens , Additions and much more . Give us a try , we do great work and are very passionate about what we do.</p>
</section>

<section>
  <svg class="abs services-bg" viewBox="0 0 1200 455" role="img" aria-label="Green backdrop with a builder at work">
    <defs>
      <linearGradient id="svcg" x1="0" y1="0" x2="1" y2="1"><stop offset="0" stop-color="#0f7a44"/><stop offset=".55" stop-color="#0c6a3b"/><stop offset="1" stop-color="#0a5a33"/></linearGradient>
      <radialGradient id="svcglow" cx=".8" cy=".3" r=".5"><stop offset="0" stop-color="#2c9a60" stop-opacity=".55"/><stop offset="1" stop-color="#2c9a60" stop-opacity="0"/></radialGradient>
    </defs>
    <path d="M0 80 Q600 0 1200 80 L1200 455 L0 455 Z" fill="url(#svcg)"/>
    <path d="M0 80 Q600 0 1200 80 L1200 455 L0 455 Z" fill="url(#svcglow)"/>
    <path d="M180 40 Q640 -18 1200 60 Q640 6 180 40 Z" fill="#2b3f78"/>
  </svg>
  <h2 class="abs section-title services-title">Our Services</h2>
  <div class="abs services-underline"></div>
  <div class="abs service-card" style="left:92px"><div class="photo" role="img" aria-label="Freshly painted room" style="background:radial-gradient(ellipse 50% 40% at 40% 35%,#eef0f0,rgba(238,240,240,0) 70%),linear-gradient(170deg,#c9cfcf 0%,#a9b1b1 55%,#7f8888 100%)"></div><div class="caption">Painting</div></div>
  <div class="abs service-card" style="left:342px"><div class="photo" role="img" aria-label="Marble-tiled bathroom with tub" style="background:radial-gradient(ellipse 45% 25% at 45% 72%,#f2efe8,rgba(242,239,232,0) 70%),linear-gradient(160deg,#d2a868 0%,#a87a42 50%,#6e4a24 100%)"></div><div class="caption">Bathrooms</div></div>
  <div class="abs service-card" style="left:592px"><div class="photo" role="img" aria-label="Kitchen with wooden cabinets" style="background:linear-gradient(180deg,#e6dccb 0%,#c9a476 35%,#5f8a86 62%,#c29a6c 100%)"></div><div class="caption">Kitchens</div></div>
  <div class="abs service-card" style="left:842px"><div class="photo" role="img" aria-label="Wooden framing for windows and doors" style="background:radial-gradient(ellipse 30% 40% at 35% 35%,#eedcbc,rgba(238,220,188,0) 70%),linear-gradient(150deg,#c89460 0%,#9a6636 55%,#5e3a1c 100%)"></div><div class="caption">Windows and Doors</div></div>
</section>

<section>
  <div class="abs why-photo" role="img" aria-label="Finished basement with wood flooring"></div>
  <h2 class="abs why-title">Why Choose Us</h2>
  <div class="abs why-text">
    <p>Fusce ultricies orci ac feugiat suscipit leo massa sodales velit et scelerisque mi tortor at ipsum aligula augue</p>
    <p>elit Integer congue augue et malesuada iaculis ipsum dui aliquet felis at cursus magna nisl nec elit Praesent elementum elit at tellus nec ultricies sit amet porttitor mattis enim In massa libero interdum nec interdum vel blandit sed nulla in ullamcorper</p>
  </div>
  <div class="abs btn">READ MORE</div>
</section>

<section>
  <div class="abs licensed"></div>
  <h2 class="abs section-title licensed-title">Licensed &amp; Insured</h2>
  <ul class="abs trade-list" style="left:130px;top:1962px"><li>Ceramic Flooring</li><li>Marble Flooring</li><li>Hardwood Flooring</li><li>Doors</li></ul>
  <ul class="abs trade-list" style="left:388px;top:1962px"><li>Windows</li><li>Sheetrock</li><li>Kitchens</li><li>Bathrooms</li></ul>
  <ul class="abs trade-list" style="left:635px;top:1962px"><li>Painting</li><li>Plaster</li><li>Cement</li><li>Decks</li></ul>
  <ul class="abs trade-list" style="left:862px;top:1962px"><li>Pavers</li><li>Additions</li><li>Basements</li></ul>
</section>

<section>
  <div class="abs gallery"></div>
  <h2 class="abs section-title gallery-title">Our Gallery</h2>
  <div class="abs gallery-item" style="left:130px"><div class="photo" role="img" aria-label="Deck with white railing" style="background:linear-gradient(180deg,#f2f2f0 0%,#dcdcd8 35%,#6a625a 55%,#4a433d 100%)"></div></div>
  <div class="abs gallery-item" style="left:373px"><div class="photo" role="img" aria-label="Patio concrete surface" style="background:radial-gradient(ellipse 60% 50% at 50% 60%,#9a8e86,rgba(154,142,134,0) 75%),linear-gradient(170deg,#5a4f48 0%,#7c716a 40%,#6a5f58 100%)"></div></div>
  <div class="abs gallery-item" style="left:614px"><div class="photo" role="img" aria-label="Drill fastening deck boards" style="background:radial-gradient(ellipse 25% 35% at 45% 30%,#b84a3a,rgba(184,74,58,0) 70%),linear-gradient(160deg,#a4a4a4 0%,#7a7a7a 50%,#4c4c4c 100%)"></div></div>
  <div class="abs gallery-item" style="left:855px"><div class="photo" role="img" aria-label="Laying brick pavers" style="background:radial-gradient(ellipse 25% 20% at 72% 45%,#f4f4f4,rgba(244,244,244,0) 70%),linear-gradient(160deg,#d08466 0%,#b0604a 50%,#7e4232 100%)"></div></div>
</section>

<footer>
  <div class="abs site-footer"></div>
  <h3 class="abs footer-head" style="left:116px;top:2682px">Quick Links</h3>
  <ul class="abs footer-links" style="left:118px;top:2720px"><li>Home</li><li>About us</li><li>Our Services</li><li>Why Us</li><li>Gallery</li></ul>
  <ul class="abs footer-links" style="left:305px;top:2732px"><li>FAQ</li><li>Testimonials</li><li>Locations</li><li>Blogs</li><li>Contact Us</li></ul>
  <h3 class="abs footer-head" style="left:495px;top:2680px">Contact Us</h3>
  <div class="abs footer-contact" style="left:497px;top:2720px">
    <p>412 Millbrook Avenue Suite 210</p>
    <p>Ashford, PA 19000</p>
    <p class="row" style="margin-top:6px"><svg width="15" height="15" viewBox="0 0 24 24"><path fill="#0b5e36" d="M6.6 10.8a15 15 0 006.6 6.6l2.2-2.2a1 1 0 011-.25 11.4 11.4 0 003.6.6 1 1 0 011 1V20a1 1 0 01-1 1A17 17 0 013 4a1 1 0 011-1h3.5a1 1 0 011 1c0 1.25.2 2.45.57 3.57a1 1 0 01-.25 1z"/></svg>(667) 555-0192</p>
    <p class="row"><svg width="15" height="12" viewBox="0 0 24 18"><rect width="24" height="18" rx="2" fill="#0b5e36"/><path d="M1 2l11 8 11-8" stroke="#fff" stroke-width="2" fill="none"/></svg>info@companyname.com</p>
  </div>
  <h3 class="abs footer-head" style="left:810px;top:2680px">Follow Us</h3>
  <nav class="abs socials" aria-label="Social media links">
    <a aria-label="Social link 1"></a><a aria-label="Social link 2"></a><a aria-label="Social link 3"></a><a aria-label="Social link 4"></a><a aria-label="Social link 5"></a>
  </nav>
  <div class="abs footer-brand"><span class="brand-mark"></span><span class="brand-name">Bramble Fork Builders LLC</span></div>
  <div class="abs footer-rule"></div>
  <p class="abs copyright">© 2017 Company Name &nbsp;All right reserved &nbsp;Term of Use</p>
</footer>

</body>
</html>
```